Calvoterra business card

a nice business card with the logo,
Calvoterra
Teresa Lindqvist
Marketing Director
CH-1563 Geneva
Switzerland
+41 76 382 1904
email: Teresa.Lindqvist@calvoterra-mail.example

Target Market(s)

fertilizer business people, very nice and classic business card, normal size, make it nice and funky, try to make it different from the normal boring ones if possible.

Industry/Entity Type

Farming

Number of Pages Required

1 page

Requirements
Must have
• logo, Calvoterra, my name - mail and phone number
regular business card size for me to print easy please

```html
<!DOCTYPE html>
<html lang="en">
<head>
<meta charset="utf-8">
<title>Calvoterra – Business Card</title>
<link rel="stylesheet" href="https://fonts.googleapis.com/css2?family=Arimo:wght@400;700&display=swap">
<style>
  :root {
    --backdrop: #e4e4e4;
    --card-paper: #ffffff;
    --card-edge: #9a9a9a;
    --leaf-green: #aef01e;
    --leaf-green-soft: #c4f55a;
    --signal-green: #36f000;
    --ink-slate: #5b6270;
    --brand-grey: #8e9ba6;
  }
  * { margin: 0; padding: 0; box-sizing: border-box; }
  html, body {
    width: 930px;
    height: 1200px;
    overflow: hidden;
    background: var(--backdrop);
    font-family: "Arimo", Arial, sans-serif;
  }
  .canvas {
    position: relative;
    width: 930px;
    height: 1200px;
  }
  .business-card {
    position: absolute;
    left: 268px;
    top: 407px;
    width: 383px;
    height: 217px;
    background: var(--card-paper);
    border: 1px solid var(--card-edge);
    overflow: hidden;
  }
  .brand-block {
    position: absolute;
    left: 22px;
    top: 30px;
    width: 80px;
    display: flex;
    flex-direction: column;
    align-items: center;
  }
  .brand-dot {
    width: 26px;
    height: 26px;
    border-radius: 50%;
    background: var(--leaf-green);
    margin-top: 8px;
  }
  .brand-name {
    margin-top: 30px;
    font-size: 5px;
    letter-spacing: 2.4px;
    text-transform: uppercase;
    color: var(--brand-grey);
    font-weight: 400;
    white-space: nowrap;
  }
  .contact-block {
    position: absolute;
    left: 212px;
    top: 31px;
    color: var(--ink-slate);
  }
  .person-name {
    font-size: 13px;
    font-weight: 700;
    color: var(--signal-green);
    line-height: 16px;
  }
  .person-role {
    font-size: 9.5px;
    font-weight: 700;
    line-height: 12px;
    margin-top: 3px;
  }
  .contact-lines {
    list-style: none;
    margin-top: 13px;
    font-size: 9.5px;
    line-height: 13.8px;
  }
  .contact-email {
    font-size: 8px;
    white-space: nowrap;
  }
  .colour-band {
    position: absolute;
    left: 0;
    right: 0;
    bottom: 0;
    height: 58px;
    background: linear-gradient(180deg, var(--leaf-green-soft) 0%, var(--leaf-green) 100%);
  }
</style>
</head>
<body>
<main class="canvas">
  <article class="business-card">
    <div class="colour-band" role="img" aria-label="Decorative lime green wave band along the bottom of the card"></div>

    <div class="brand-block">
      <span class="brand-dot"></span>
      <span class="brand-name">Calvoterra</span>
    </div>

    <div class="contact-block">
      <h1 class="person-name">Teresa Lindqvist</h1>
      <p class="person-role">Marketing Director</p>
      <ul class="contact-lines">
        <li>CH-1563 Geneva</li>
        <li>Switzerland</li>
        <li>+41 76 382 1904</li>
        <li class="contact-email">Teresa.Lindqvist@calvoterra-mail.example</li>
      </ul>
    </div>
  </article>
</main>
</body>
</html>
```